Flyer, poster, banner and social media titles designs for Crisis Rebuilding Tentes

The Common Tenets for Crisis Rebuilding provide a nationally agreed framework to guide recovery policy and practice across Australia. The Principles support recovery practitioners, governments, non-government organisations and communities to deliver effective, community-centred recovery outcomes.
The Principles have recently been refreshed through extensive consultation and we require a contemporary visual identity and design suite that will increase awareness, engagement and practical application of the Principles.
The redesign will cover:
• A4 Brochure (primary publication)
• A3 Poster
• Pull up banner
• Social Media Tiles
The new design should:
• Create a recognisable brand for the Common Tenets.
• Appeal to both experienced and emerging recovery practitioners.
• Reflect contemporary disaster recovery practice.
• Feel people-focused rather than government-focused.
• Support future resources such as videos, implementation guides, presentations and workshop materials.
• Remain relevant for several years without requiring a major redesign.
Target Audience
• Disaster recovery practitioners
• Government agencies
• Non-government organisations
• Community recovery workers
• Recovery managers and leaders
• Community stakeholders and volunteers
The visual identity should reflect the six Principles:
• Understanding Context
• Recognising Complexity
• Community-Centred Approaches
• Coordination
• Communication
• Capacity Building
The design should communicate:
• Recovery is centred on people and communities.
• Recovery is collaborative and involves many sectors.
• Recovery is adaptive, inclusive and evidence-informed.
• Recovery supports resilience and long-term wellbeing.
• The Principles provide practical guidance for recovery practice.
We are looking for:
• Modern and professional
• Warm and approachable
• Human-centred
• Inclusive and accessible
• Australian in context
• Visually engaging
• Suitable for print and digital use
We would like to avoid:
• Images of disaster destruction
• Emergency response imagery (fire trucks, flashing lights, etc.)
• Overly corporate or bureaucratic designs
• Designs that focus on deficits rather than recovery and growth
Consider themes such as:
• Connection and collaboration
• Communities and people
• Growth, recovery and renewal
Accessibility
Designs should:
• Meet accessibility best practice
• Use clear typography
• Achieve strong colour contrast
• Be suitable for both digital and print formats

Deliverables
1. Principles Brochure
• A4 trifold size x 2 (online and print friendly version)
• A side to include cover side, logos side and overview of principles.
• B side full details of the principles
• Graphic to highlight the 3 c’s concept (RECOVERY Context, complexity, community centred, coordinate, communicate and capacity). Currently 3 circles.
• Can be printed and distributed electronically
2. Poster
• A1 and A3 versions
• Suitable for office and workshop display
3. Pull-Up Banner - 850 mm (W) × 2000 mm (H)
• Conference and event use
• High visual impact
• Strong branding and concise messaging
4. Social Media Tiles x 3
Updates

We are providing an extension and increasing the budget following feedback from designers. We are wanting the resources to look and feel different from the existing designs, considering either a different colour palette in the designs or different motif with the leave design. Any nature based designs should consider the Australian fauna or flora. Also suggest avoiding images in the designs. The principles are not numbered or liner in the concept of how they function. Happy to answer any further questions and thank you for your suggested concepts.

Target Market(s)

Disaster recovery practitioners, Government agencies , Non-government organisations, Community recovery workers and Community stakeholders and volunteers

Industry/Entity Type

Disaster recovery

Colors

Designer to choose colors to be used in the design.

Requirements
Must have
• Modern, warm, visually engaging, human-centred, Australian in context and different to the current design.
Nice to have
• Symbols for each principles
Should not have
• Images of disaster destruction, Emergency response imagery, Overly corporate or bureaucratic designs, Designs that focus on deficits rather than recovery and growth, avoid too much black

```html
<!DOCTYPE html>
<html lang="en">
<head>
<meta charset="utf-8">
<title>Common Tenets for Crisis Rebuilding – Social Tiles</title>
<link href="https://fonts.googleapis.com/css2?family=Outfit:wght@300;400;600;700&family=Allura&display=swap" rel="stylesheet">
<style>
  :root{
    --board:#8aaad5;
    --ink:#2b2b2b;
    --green:#4a7d2a;
    --green-bright:#4fae3c;
    --sage:#7c9a7c;
    --tan:#e6d6c2;
    --brown:#7a5a2c;
    --gold:#b59a57;
    --gold-pale:#efe6cf;
    --cream:#faf4ed;
    --stone:#eeedea;
    --line-art:#ebebe4;
    --leaf:#a9bcaa;
  }
  *{box-sizing:border-box;margin:0;padding:0}
  html,body{width:786px;height:1200px;overflow:hidden}
  body{background:var(--board);font-family:'Outfit',sans-serif;color:var(--ink);position:relative}
  .tile{position:absolute;left:76px;width:635px;height:330px;overflow:hidden;box-shadow:0 10px 14px rgba(40,70,120,.28)}
  .tile--cover{top:76px;background:#fff}
  .tile--landscape{top:435px;background:var(--cream)}
  .tile--botanical{top:795px;background:var(--stone)}
  .art{position:absolute}
  .script{font-family:'Allura',cursive;font-weight:400}

  /* Tile 1 */
  .pattern-band{left:0;top:0;width:100%;height:27px;background:#f1ecd8}
  .flora-left{left:0;top:30px;width:242px;height:300px;background:linear-gradient(180deg,#fff 0%,var(--line-art) 100%)}
  .flora-right{left:469px;top:55px;width:166px;height:275px;background:linear-gradient(180deg,#fff 0%,var(--line-art) 100%)}
  .cover-title{position:absolute;left:0;right:0;top:56px;text-align:center;font-size:39px;font-weight:400;line-height:39px;letter-spacing:-.6px}
  .tag{position:absolute;font-weight:700;font-size:38px;line-height:1;padding:13px 14px 16px;letter-spacing:-.5px}
  .tag--tan{left:183px;top:152px;background:var(--tan);color:var(--green);transform:rotate(-1.5deg)}
  .tag--green{left:258px;top:209px;background:var(--green);color:#fff;padding:11px 14px 13px}

  /* Tile 2 */
  .mountains{left:0;top:30px;width:318px;height:300px;background:linear-gradient(90deg,var(--gold) 0%,#c9b27f 60%,var(--cream) 100%)}
  .flora-gold{left:545px;top:0;width:90px;height:330px;background:linear-gradient(90deg,var(--cream),var(--gold-pale))}
  .landscape-copy{position:absolute;left:328px;top:42px}
  .small-title{font-size:17px;line-height:21px;letter-spacing:-.3px}
  .landscape-copy .script{display:block;color:var(--green-bright);font-size:42px;line-height:40px;margin-top:24px}
  .caps{font-size:32px;line-height:33px;text-transform:uppercase;letter-spacing:-.7px;margin-top:4px}
  .caps b{font-weight:700;color:var(--green)}
  .caps span{font-weight:300}
  .caps .fade{color:var(--sage);font-weight:700}

  /* Tile 3 */
  .plant{left:212px;top:0;width:423px;height:330px;background:linear-gradient(90deg,var(--stone) 0%,var(--leaf) 55%,#8fa791 100%)}
  .botanical-copy{position:absolute;left:47px;top:84px}
  .botanical-title{font-size:35px;line-height:33px;font-weight:400;letter-spacing:-.7px}
  .botanical-title b{font-weight:700;color:var(--green)}
  .botanical-title .script{color:var(--green);font-size:48px;margin-left:4px}
  .rule{display:flex;width:179px;height:2px;margin-top:24px}
  .rule i{flex:1;background:var(--brown)}
  .rule i+i{background:var(--green-bright)}
  .sub{font-size:22px;line-height:29px;margin-top:14px;letter-spacing:-.3px}
  .sub .g{color:var(--green)}
  .sub .s{color:var(--sage)}
</style>
</head>
<body>
  <section class="tile tile--cover">
    <div class="art pattern-band" role="img" aria-label="Decorative band of pale botanical tile motifs"></div>
    <div class="art flora-left" role="img" aria-label="Line drawing of lilies and leafy stems"></div>
    <div class="art flora-right" role="img" aria-label="Line drawing of lilies and leafy stems"></div>
    <h1 class="cover-title">Common<br>Tenets for</h1>
    <span class="tag tag--tan">Crisis</span>
    <span class="tag tag--green">Rebuilding</span>
  </section>

  <section class="tile tile--landscape">
    <div class="art mountains" role="img" aria-label="Golden sketch of mountains, pine forest, moon and birds"></div>
    <div class="art flora-gold" role="img" aria-label="Fine gold line drawing of flowering stems"></div>
    <div class="landscape-copy">
      <p class="small-title">Common Tenets for<br>Crisis Rebuilding</p>
      <span class="script">working together</span>
      <p class="caps"><span>To</span> <b>Help</b><br><b>Communities</b><br><b>Recover</b> <span>From</span><br><span class="fade">Disaster</span></p>
    </div>
  </section>

  <section class="tile tile--botanical">
    <div class="art plant" role="img" aria-label="Photograph of a potted eucalyptus plant against a pale wall"></div>
    <div class="botanical-copy">
      <h2 class="botanical-title">Common<br>Tenets for<br><b>Crisis</b><span class="script">rebuilding</span></h2>
      <div class="rule"><i></i><i></i></div>
      <p class="sub">To <span class="g">help communities</span><br><span class="g">recover</span> from <span class="s">disaster</span></p>
    </div>
  </section>
</body>
</html>
```